Spa Business Card Design Project

Hello! We are a boutique spa for men and women that is rebranding. I would like a memorable new business card that showcases our beautiful new logo and our unique business. I would like it to be classic/timeless and eclectic/artistic at the  same time.
I am a fan of negative space as you can tell from the logo. I am also open to any creative ideas.
Multi sided design. Two sided design is acceptable as an option, too. "Flaps/folds/whatever the design term is" are optional- whether full vertical or horizontal, half flap, full flap etc
On either side next to the golden snail I would potentially like to see "slow down. Enjoy Life."  Possibly on one statment on top of each other, crowned with the snail. Or the statment following the snail on one line... I am open for a creative suprise, too.
The back I would like room for the standard Information
"3817 Birch Lane
Fernhill, Vermont 05342
(518) 462 3085
info@thecorvella spa.com
The snail is to be done in gold ink.
Can I also Have an option for cards that are individualized for staff members, too?

Updates
Project Deadline Extended
Reason: I apologize for the deadline extension. My day was more involved than anticipated in other matters. Hope to have this closed by next Tuesday.
Thank you

Target Market(s)
Men and women with expendable income between the ages of 30-55
Industry/Entity Type
Boutique
Requirements
Must have
- only black and gold ink.

Nice to have
- One of a kind.
Showcase the snail :-)
make you smile :-)
Fun, but professional.
Should not have
- Lots of color.
Too feminine.
Too busy.

```html
<!DOCTYPE html>
<html lang="en">
<head>
<meta charset="utf-8">
<title>The Corvella Spa – Business Card</title>
<link rel="stylesheet" href="https://fonts.googleapis.com/css2?family=Cinzel:wght@500&family=Cormorant+Garamond:ital,wght@1,500&family=Questrial&display=swap">
<style>
  :root {
    --page: #f4f4f2;
    --card: #ffffff;
    --gold: #d3ab4f;
    --ink: #141414;
    --slate: #5a6562;
    --shadow: rgba(0, 0, 0, 0.12);
  }
  * { box-sizing: border-box; margin: 0; padding: 0; }
  html, body {
    width: 1200px;
    height: 1000px;
    overflow: hidden;
    background: var(--page);
  }
  .sheet {
    position: relative;
    width: 1200px;
    height: 1000px;
  }
  .card {
    position: absolute;
    left: 250px;
    width: 700px;
    height: 400px;
    background: var(--card);
    box-shadow: 0 6px 18px var(--shadow);
  }
  .card--front { top: 60px; }
  .card--back  { top: 540px; }
  .card__rule {
    position: absolute;
    left: 0;
    right: 0;
    height: 6px;
    background: var(--gold);
  }
  .card__rule--top { top: 28px; }
  .card__rule--bottom { bottom: 28px; }

  /* Front */
  .brand {
    position: absolute;
    inset: 0;
    display: flex;
    flex-direction: column;
    align-items: center;
    justify-content: center;
  }
  .brand__name {
    font-family: "Cinzel", serif;
    font-weight: 500;
    font-size: 56px;
    letter-spacing: 3px;
    color: var(--ink);
    line-height: 1.05;
    text-align: center;
  }
  .brand__tagline {
    margin-top: 22px;
    font-family: "Questrial", sans-serif;
    font-size: 22px;
    color: var(--ink);
    letter-spacing: 0.5px;
  }

  /* Back */
  .mascot {
    position: absolute;
    left: 40px;
    top: 90px;
    width: 290px;
    height: 170px;
    border-radius: 85px 85px 10px 30px;
    background: var(--gold);
  }
  .motto {
    position: absolute;
    left: 40px;
    top: 290px;
    width: 300px;
    font-family: "Cormorant Garamond", serif;
    font-style: italic;
    font-weight: 500;
    font-size: 21px;
    letter-spacing: 0.5px;
    color: var(--slate);
    text-transform: uppercase;
    white-space: nowrap;
  }
  .contact {
    position: absolute;
    left: 360px;
    top: 95px;
    width: 310px;
    font-family: "Cormorant Garamond", serif;
    font-style: italic;
    font-weight: 500;
    font-size: 24px;
    line-height: 1.25;
    color: var(--slate);
    text-align: center;
    white-space: nowrap;
  }
  .contact__phone { margin-top: 44px; }
  .contact__email { margin-top: 38px; }
</style>
</head>
<body>
<main class="sheet">
  <section class="card card--front" aria-label="Card front">
    <div class="card__rule card__rule--top"></div>
    <div class="brand">
      <div class="brand__name">The Corvella<br>Spa</div>
      <div class="brand__tagline">a boutique spa for Men &amp; Women</div>
    </div>
    <div class="card__rule card__rule--bottom"></div>
  </section>

  <section class="card card--back" aria-label="Card back">
    <div class="card__rule card__rule--top"></div>
    <div class="mascot" role="img" aria-label="Gold snail illustration"></div>
    <p class="motto">Slow down. Enjoy life.</p>
    <address class="contact">
      <div class="contact__street">3817 Birch Lane</div>
      <div class="contact__city">Fernhill, Vermont 05342</div>
      <div class="contact__phone">(518) 462 3085</div>
      <div class="contact__email">info@thecorvella spa.com</div>
    </address>
    <div class="card__rule card__rule--bottom"></div>
  </section>
</main>
</body>
</html>
```